We want to design total new business card and logo for Kestrel Building Services Ltd

Our company name Kestrel Building Services Ltd. Design new logo and business card , need hi-end luxury style art for architecture and construction industry. The card should simple but stylish. Our business focus on CONNECT tradesman to construction company, help marketing construction company tender oversea projects, managing franchise in construction sector, delivery amazing services to our client, so Logo should show the CONNECTION IDEA, CONNECTING PEOPLE, LUXURY. Visit our website for more information: kestrelhub.co.nz

Low design quality

Target Market(s)

Directors or managers

Industry/Entity Type

Construction Company

Contact Information for Business Card

Name, Title, Mobile, Email, Website

Font styles to use
Serif

Colors

Designer to choose colors to be used in the design.

Requirements
Must have
• Simple and luxury, connection icon
Nice to have
• Special materials, plastic card, look through,...
• Look new ideas.

```html
<!DOCTYPE html>
<html lang="en">
<head>
<meta charset="utf-8">
<title>Kestrel Building Services Ltd — Business Card</title>
<link rel="stylesheet" href="https://fonts.googleapis.com/css2?family=Cinzel:wght@600&family=Lato:wght@400;700&display=swap">
<style>
  :root {
    --stage: #1c1c1c;
    --card: #151515;
    --card-edge: #262626;
    --white: #f2f2f2;
    --silver: #b8b8b8;
    --blue: #3b7cc9;
  }
  * { box-sizing: border-box; margin: 0; padding: 0; }
  html, body { width: 1200px; height: 1200px; overflow: hidden; }
  body {
    background: radial-gradient(ellipse at 60% 30%, #2a2a2a 0%, var(--stage) 60%, #111 100%);
    font-family: "Lato", Arial, sans-serif;
    position: relative;
  }
  .card {
    position: absolute;
    left: 150px;
    width: 900px;
    height: 514px;
    background: var(--card);
    border: 1px solid var(--card-edge);
    border-radius: 28px;
    box-shadow: 0 20px 50px rgba(0,0,0,0.6);
  }
  .card--front { top: 60px; display: flex; align-items: center; justify-content: center; }
  .card--back { top: 626px; display: flex; align-items: center; }

  .brand { display: flex; flex-direction: column; align-items: center; }
  .brand__shape {
    width: 70px;
    height: 70px;
    background: var(--silver);
    margin-bottom: 22px;
  }
  .brand__name {
    font-family: "Cinzel", "Times New Roman", serif;
    font-weight: 600;
    text-transform: uppercase;
    text-align: center;
    letter-spacing: 2px;
    line-height: 1.2;
  }
  .card--front .brand__name { font-size: 44px; color: var(--silver); }
  .card--front .brand__shape { width: 84px; height: 84px; }
  .card--back .brand__name { font-size: 30px; color: var(--white); }
  .card--back .brand__shape { background: var(--blue); }

  .brand-block { width: 450px; display: flex; justify-content: center; padding-left: 40px; }
  .divider { width: 2px; height: 180px; background: var(--blue); margin: 0 44px 0 20px; }

  .contact { color: var(--white); }
  .contact__name { font-size: 34px; font-weight: 700; color: var(--blue); letter-spacing: 1px; text-transform: uppercase; }
  .contact__title { font-size: 20px; text-transform: uppercase; letter-spacing: 1px; margin-bottom: 22px; }
  .contact__list { list-style: none; font-size: 20px; }
  .contact__list li { display: flex; align-items: center; gap: 14px; margin-bottom: 8px; }
  .contact__list svg { width: 20px; height: 20px; flex: none; }
</style>
</head>
<body>
  <section class="card card--front">
    <div class="brand">
      <div class="brand__shape"></div>
      <div class="brand__name">Kestrel Building<br>Services Ltd</div>
    </div>
  </section>

  <section class="card card--back">
    <div class="brand-block">
      <div class="brand">
        <div class="brand__shape"></div>
        <div class="brand__name">Kestrel Building<br>Services Ltd</div>
      </div>
    </div>
    <div class="divider"></div>
    <div class="contact">
      <div class="contact__name">Daniel Harrow</div>
      <div class="contact__title">Managing Director</div>
      <ul class="contact__list">
        <li>
          <svg viewBox="0 0 24 24" aria-hidden="true"><path fill="#3b7cc9" d="M6.6 10.8a15.2 15.2 0 0 0 6.6 6.6l2.2-2.2a1 1 0 0 1 1-.25 11.4 11.4 0 0 0 3.6.57 1 1 0 0 1 1 1V20a1 1 0 0 1-1 1A17 17 0 0 1 3 4a1 1 0 0 1 1-1h3.5a1 1 0 0 1 1 1c0 1.25.2 2.45.57 3.57a1 1 0 0 1-.25 1z"/></svg>
          021-548-3097
        </li>
        <li>
          <svg viewBox="0 0 24 24" aria-hidden="true"><rect x="2" y="5" width="20" height="14" rx="1.5" fill="#3b7cc9"/><path d="M3 6l9 7 9-7" fill="none" stroke="#151515" stroke-width="1.8"/></svg>
          daniel@kestrelhub.co.nz
        </li>
        <li>
          <svg viewBox="0 0 24 24" aria-hidden="true" fill="none" stroke="#3b7cc9" stroke-width="2"><circle cx="12" cy="12" r="9"/><ellipse cx="12" cy="12" rx="4" ry="9"/><path d="M3 12h18M5 7h14M5 17h14"/></svg>
          www.kestrelhub.co.nz
        </li>
      </ul>
    </div>
  </section>
</body>
</html>
```